Counseling Practice Business Card

I need a professional looking business card incorporating my new logo that was just completed. Card needs to incorporate my name and title, description of my specialty, my address, my phone number, my fax number, my email and my website URL. I need to be able to choose design on/with different paper colors and textures.
I do not have a lot of business card ideas so I am open to anything but I want bold,sharp, clear card without additional designs other than my logo (see attached file info). I am open to different color backgrounds or paper colors including black. I do not like traditional brackets around area codes in phone number or dashes between numbers in phone number. Am open to other ways of presenting including periods between numbers as appropriate. I do not know enough to know what I like yet but I want card to coordinate and work together with my logo. My practice emphasizes natural mental health interventions so any use of color (with background paper color or the blue and green in my logo) that elicits nature is nice. In addition to black, any natural brown or wood looking background might be desirable also. Most of the offerings so far look very similar and boring.

Target Market(s)

Potential therapy clients and other professionals

Contact Information for Business Card

Card information:
Marcus T. Whitfield, Ph.D.
Licensed Clinical Psychologist
Integrative Health Coach
4812 Ferndale Pkwy NW
Suite 730
Duluth, GA 30096
(770) 555-0142 phone
(770) 555-0186 fax
drmarcuswhitfield@kelvora.com
pathbloomcounseling.com

Font styles to use
Serif
Sans Serif
Other font styles liked:
• anything that you think looks crisp, clear and easily readable

Requirements
Must have
• Any color used should coordinate with my logo design (see attached files).
• Card should be printed horizontally so top and bottom are longest sides of rectangle.
• Background color or paper color should complement and highlight logo. Do not like a white background. black, grey, brown or any color my logo would blend well with.
Nice to have
• I would like designer to utilize color to highlight letters/name or phone-fax-web symbols.
• Bottom edge of card could be highlighted if appropriate to an idea.
Should not have
• I would NOT want the card to have a pure white background at all.
• No clear cards.
• Cards should be oriented with long sides on bottom and top, NOT sides. DO NOT LIKE THIS THIN TALL ORIENTATION.

```html
<!DOCTYPE html>
<html lang="en">
<head>
<meta charset="utf-8">
<title>Pathbloom Counseling – Business Card</title>
<link rel="stylesheet" href="https://fonts.googleapis.com/css2?family=Roboto:wght@400;500&family=Roboto+Condensed:wght@700&display=swap">
<style>
  :root {
    --backdrop: #e9e4dc;
    --card-black: #121316;
    --brand-blue: #2a74b8;
    --brand-green: #046a34;
    --text-light: #ffffff;
    --url-light: #c9d6e6;
  }
  * { margin: 0; padding: 0; box-sizing: border-box; }
  html, body { width: 1200px; height: 960px; overflow: hidden; }
  body {
    position: relative;
    background: var(--backdrop);
    font-family: "Roboto", Arial, sans-serif;
  }
  .card {
    position: absolute;
    width: 600px;
    height: 343px;
    background: var(--card-black);
    box-shadow: 0 3px 8px rgba(0,0,0,0.35);
    overflow: hidden;
  }
  .card-front { left: 314px; top: 113px; }
  .card-back { left: 312px; top: 472px; }

  .brand-name {
    position: absolute;
    color: var(--brand-blue);
    font-weight: 500;
    text-align: center;
    line-height: 1.05;
  }
  .card-front .brand-name { left: 0; width: 289px; top: 146px; font-size: 30px; }
  .card-front .brand-name span { display: block; font-size: 30px; }
  .card-back .brand-name { left: 0; width: 600px; top: 118px; font-size: 46px; }

  .divider-stripe {
    position: absolute;
    left: 289px; top: 0;
    width: 15px; height: 100%;
    background: linear-gradient(to right,
      var(--brand-blue) 0 7px, var(--card-black) 7px 9px, var(--brand-blue) 9px 15px);
  }
  .details-panel {
    position: absolute;
    left: 304px; top: 0;
    width: 296px; height: 100%;
    background: var(--brand-green);
    color: var(--text-light);
    padding: 54px 0 0 18px;
  }
  .person-name {
    font-family: "Roboto Condensed", Arial, sans-serif;
    font-weight: 700;
    font-size: 21px;
    text-transform: uppercase;
    line-height: 1.1;
  }
  .person-title { font-size: 15px; font-weight: 500; line-height: 19px; }
  .dotted-rule {
    width: 210px;
    margin: 10px 0 12px 6px;
    border-top: 2px dotted rgba(255,255,255,0.85);
  }
  .address { font-size: 14px; line-height: 18px; padding-left: 2px; }
  .contact-list { list-style: none; font-size: 14.5px; line-height: 19.3px; }
  .contact-list li { display: flex; align-items: center; }
  .contact-list svg { width: 12px; height: 12px; margin-right: 10px; fill: var(--text-light); }

  .web-band {
    position: absolute;
    left: 0; top: 279px;
    width: 100%; height: 30px;
    background: var(--brand-blue);
    color: var(--url-light);
    font-size: 14px;
    letter-spacing: 3.6px;
    text-align: center;
    line-height: 30px;
  }
</style>
</head>
<body>
  <section class="card card-front">
    <div class="brand-name">Pathbloom<span>Counseling</span></div>
    <div class="divider-stripe"></div>
    <div class="details-panel">
      <h1 class="person-name">Marcus T. Whitfield, Ph.D.</h1>
      <p class="person-title">Licensed Clinical Psychologist</p>
      <p class="person-title">Integrative Health Coach</p>
      <div class="dotted-rule"></div>
      <p class="address">4812 Ferndale Pkwy NW<br>Suite 730 Duluth, GA 30096</p>
      <div class="dotted-rule"></div>
      <ul class="contact-list">
        <li><svg viewBox="0 0 24 24" aria-hidden="true"><path d="M6.6 10.8a15.1 15.1 0 0 0 6.6 6.6l2.2-2.2c.3-.3.7-.4 1-.2 1.1.4 2.3.6 3.6.6.6 0 1 .4 1 1V20c0 .6-.4 1-1 1A17 17 0 0 1 3 4c0-.6.4-1 1-1h3.5c.6 0 1 .4 1 1 0 1.3.2 2.5.6 3.6.1.3 0 .7-.2 1z"/></svg>(770) 555-0142</li>
        <li><svg viewBox="0 0 24 24" aria-hidden="true"><path d="M6 2h12v5H6zM3 8h18a1 1 0 0 1 1 1v8h-4v5H6v-5H2V9a1 1 0 0 1 1-1zm5 8v4h8v-4z"/></svg>(770) 555-0186</li>
        <li><svg viewBox="0 0 24 24" aria-hidden="true"><path d="M2 5h20v14H2zm2 2v.5l8 5 8-5V7l-8 5z"/></svg>drmarcuswhitfield@kelvora.com</li>
        <li><svg viewBox="0 0 24 24" aria-hidden="true"><circle cx="12" cy="12" r="10"/></svg>www.pathbloomcounseling.com</li>
      </ul>
    </div>
  </section>

  <section class="card card-back">
    <div class="brand-name">Pathbloom Counseling</div>
    <div class="web-band">www.pathbloomcounseling.com</div>
  </section>
</body>
</html>
```